I want an upgrade / face-lift to the all the pages and sections of the current website at vorenta.net. I am a developer but not a designer.

The website layout does not need to stay the same. Only the text, buttons, links, etc, need to stay the same. Logo can also be changed or altered.

1) Header
* Logo
* Tagline - Friends of the Messianic Community in Israel
* Short explanation - Vorenta.net aggregates new links from 113 websites of the Messianic Community in Israel. Learn more
* Login button
* Language Links (or picker) - English, Hebrew, Chinese (this currently isn't on Vorenta.net)

2) Nav Bar - no dropdowns
* Newsfeed
* Israel Directory
* International Directory
* Product Directory
* Website Directory

3) Sidebar
* Text - Sign up to Vorenta.net to receive a weekly email of new articles and videos from the Messianic community in Israel.
* Sign up button
* Brixo Ads or other Ads

4) List of Newsfeed links - (this is the main content of the homepage. Note the links go to other websites. It's not blog entries)
* Image
* Link Title
* website
* author (optional)
* date
* short description of link (optional)

5) Directory (Israel, International, Product)
* Search / Filter Bar (left vertical or horizontal ???)
* title - Israel Directory
* # of results
* A-Z
Partial for each organization
* logo
* first line - Link Name
* second link - type, city, language, area
* number of views
* description

6) Website Directory - page that lists all the websites that we crawl and gather links.
* needs upgrade / facelift

7) Organization Profile Page - click on http://vorenta.net/shalev-gate-fellowship as an example.
* all details as in list of directory, plus
* Meeting details
* contact details
* Donation details
* Donation link more prominent

8) Register Page
* include all details as on http://vorenta.net/register

9) Login Page
* include all details as on http://vorenta.net/login

10) About / FAQ / Contact pages
* include all details as on http://vorenta.net/about
* include all details as on http://vorenta.net/faq
* include all details as on http://vorenta.net/contact

11) Footer
* * include all details as on as website
About | Newsfeed | Israel Directory | International Directory | Product Directory | Website Directory | Contact
©2006–2013 Vorenta.net All rights reserved
Vorenta is a Hebrew word that means "community" or "congregation"

12) Bonus - Email Newsletter Design
* I want to send out 5 -10 new newsfeed links each weeks
* It should be similar to the newsfeed page, but for e-newsletters. I read that the css must for different and tables are preferred about for email.

The following pages appear for logged in users only
13) List of Ads
14) List of Events
15) Ad Single Page
16) Event Single Page
17) Edit Ad Form
18) Edit Event Form
19) Edit Organization Form
20) Edit User Information Form

Reason: First project. I originally entered 2 days, but am extending to 10 days.

I removed the requirement to delivery HTML/CSS and I static design of all pages is acceptable to win the project.  This is my first project and I wasn't aware that PixelHarbor focuses on static design and not HTML/CSS code.

Every designer essentially used the exact same "layout" that I currently have at vorenta.net and gave it a small "facelift".  I guess my wording in the brief of the word 'facelift' was not totally accurate.  The navbar / header layout does not need to stay the same.  I would appreciate to see different options such as the navbar at the top (like www.trendolix.net) or all one color on the header (like www.gbx.net) or making the logo all white and putting it inside the blue navbar (like trendolix.net).  Just some ideas that I had.

I am willing to make the project guaranteed but most of the designs are very close to what I have now.  

Note, any ideas / graphics / images / icons that show the visitor that the website is related to Israel would be helpful.

Reason: Not enough designs received

The project is now guaranteed‎.  I hope this encourages more designers to submit and to be creative.  I look forward to seeing more designs.

I'm interested in having a background on the left and right sides for larger screens.  For an example, see http://fieldsidetally.net/

I would like to have a faded image of the Israeli flag or a creative variation of it.

This website has a background image on the right-left sides that fades as you go down

I'm looking to use the space and the right-left to give the user at a quick glance that the website deals with Israel, community, Messianic/Christian, etc.

Another style that looks good is that white/gray such as http://www.filmquillnotes.net/ and https://vestly.io/

I'm interested to see how to block out difference sections with small color variations.

Reason: some designers request that I extend since they just accepted invitation

Another design that I like.  http://gigbarn.net/

Important change.  I want the newsfeed to look like a newsfeed. Right now, it looks like a blog site.  It's not obvious that articles are from other websites in the community.  I uploaded on the brief of clipvane's feed.  It shows the a small thumbnail (16x16 or 32x32) and then user name (it my case organization name or website name) on the upper left corner above the main image. 

On the header on want to change the wording on order.  

Top row -
Vorenta (logo in big) means community in Hebrew (in small letters) 

Next row (different background color)
The Messianic Community in Israel

Next row (different background color and smaller font)
Vorenta.net aggregates new links from 100+ websites of the Messianic Community in Israel. Learn more

I uploaded a jpg file with a new header rather than what is currently on vorenta.net

Target Market(s)

Christian around the world who love Israel

Industry/Entity Type

Events

Requirements
Must have
• responsive design to be readable on mobile devices
white / gray / blue theme
Zapto-style / portal website
Nice to have
• Bootstrap 3 of Foundation
Flat-UI (also not necessary, but I like it)
Graphics, icons, etcs, related to Israel
Passion, excellence, effort and attention to details :-)
Should not have
• dark background
too much fanciness or animations

```html
<!DOCTYPE html>
<html lang="en">
<head>
<meta charset="utf-8">
<title>Vorenta.net – Friends of the Messianic Community in Israel</title>
<link href="https://fonts.googleapis.com/css2?family=Open+Sans:wght@400;600;700&family=PT+Serif:wght@700&display=swap" rel="stylesheet">
<style>
:root{
  --navy:#27324a;
  --title:#1d3b6e;
  --link:#1f5ea8;
  --text:#333;
  --muted:#888;
  --line:#dcdfe4;
  --panel:#f1f2f4;
  --blue:#2a6fc0;
  --page:#ffffff;
}
*{box-sizing:border-box;margin:0;padding:0}
html,body{width:679px;height:1200px;overflow:hidden;background:var(--page)}
body{font-family:"Open Sans",Arial,sans-serif;color:var(--text);font-size:9px;line-height:1.35;position:relative}
a{color:var(--link);text-decoration:none}

.site-header{height:44px;display:flex;align-items:center;padding:0 12px;gap:16px}
.brand{font-weight:600;font-size:15px;color:var(--navy)}
.tagline{font-family:"PT Serif",Georgia,serif;font-size:22px;color:var(--title);letter-spacing:-.2px}

.main-nav{height:19px;background:var(--navy);display:flex;padding-left:6px}
.main-nav a{color:#e4e8ef;font-size:8.5px;padding:0 20px;line-height:19px}
.main-nav a.active{background:#fff;color:var(--navy);font-weight:600;border:1px solid var(--navy)}
.intro{height:14px;background:var(--panel);font-size:7px;color:#555;text-align:center;line-height:14px;border-bottom:1px solid var(--line)}

.layout{display:flex;gap:12px;padding:8px 10px 0}
.content{width:436px}
.sidebar{width:211px}

.ph{display:block;border-radius:2px}
.hero{position:relative;height:205px;background:linear-gradient(135deg,#6e7d92,#b9c2cf 55%,#8a97a9)}
.hero-caption{position:absolute;left:0;bottom:10px;padding:6px 10px;background:rgba(20,28,44,.78);color:#fff}
.hero-caption h2{font-size:15px;font-weight:700;letter-spacing:.2px}
.hero-caption .meta{font-size:7px;color:#c9d2e0}

.grid4{display:grid;grid-template-columns:repeat(4,1fr);gap:6px;margin-top:4px}
.grid4 .ph{height:68px}
.card-title{font-size:7.5px;font-weight:700;color:#222;margin-top:3px;line-height:1.25}
.grid2{display:grid;grid-template-columns:1fr 1fr;gap:8px;margin-top:12px}
.grid2 .ph{height:106px}
.grid2 .card-title{font-size:9px;margin-top:5px}

.feed-item{display:flex;gap:10px;padding:12px 0;border-bottom:1px solid var(--line)}
.feed-item:first-of-type{margin-top:8px}
.feed-item .ph{width:94px;height:70px;flex:none}
.feed-item h3{font-size:11px;color:#222;font-weight:700}
.source{font-size:7px;color:var(--muted);display:flex;align-items:center;gap:3px;margin:2px 0 4px}
.source i{width:7px;height:7px;background:var(--link);display:inline-block}
.feed-item p{font-size:7.5px;color:#555}

.pager{display:flex;gap:2px;margin:16px 0 20px}
.pager a{border:1px solid var(--line);padding:0 4px;font-size:7px;color:#555;line-height:11px}
.pager a.on{background:var(--blue);color:#fff;border-color:var(--blue)}

.tabs{display:flex;border-bottom:1px solid var(--line);background:var(--panel)}
.tabs a{font-size:7px;color:#555;padding:3px 12px;border-right:1px solid var(--line)}
.tabs a.active{background:#fff;font-weight:700;color:#222}
.latest{list-style:none;padding:12px 0 0 16px}
.latest li{position:relative;margin-bottom:20px}
.latest li::before{content:"";position:absolute;left:-9px;top:5px;width:4px;height:4px;border-radius:50%;background:#222}
.latest b{font-size:10px;color:#222;display:block}
.latest span{font-size:7px;color:var(--muted)}

.signup{background:var(--panel);border:1px solid var(--line);padding:8px}
.signup p{font-size:7.5px;color:#444;margin-bottom:7px}
.field{height:16px;background:#fff;border:1px solid #c9ccd2;font-size:7px;color:#777;padding:0 5px;line-height:14px;margin-bottom:5px;display:flex;justify-content:space-between}
.btn{display:block;margin:4px 0 0 auto;width:58px;height:18px;background:var(--blue);color:#fff;font-size:8px;font-weight:600;text-align:center;line-height:18px;border-radius:2px}

.ad-banner{height:160px;margin-top:10px;background:linear-gradient(160deg,#1e5fb4,#4a9be0 60%,#2b73c7)}
.text-ads{border:1px solid var(--line);margin-top:8px;padding:5px 6px;background:#fafafa}
.text-ads div{margin-bottom:5px}
.text-ads b{display:block;color:var(--link);font-size:7.5px}
.text-ads p{font-size:6.5px;color:#444}
.text-ads em{font-style:normal;font-size:6.5px;color:#2a8a3a}
.ad-info{text-align:right;font-size:6px;color:var(--muted);margin-top:-2px}

.potw{margin-top:10px;border:1px solid var(--line)}
.potw h4{font-size:8.5px;background:var(--panel);padding:3px 6px;border-bottom:1px solid var(--line)}
.potw .ph{height:90px;margin:5px;background:linear-gradient(135deg,#8f98a4,#d7dbe0)}

.site-footer{position:absolute;left:0;top:1138px;width:679px;height:62px;padding:8px 12px;background:var(--panel);border-top:1px solid var(--line);font-size:7px;color:#555}
.site-footer nav a{color:var(--link)}
</style>
</head>
<body>

<header class="site-header">
  <div class="brand">Vorenta</div>
  <h1 class="tagline">Friends of the Messianic Community in Israel</h1>
</header>

<nav class="main-nav">
  <a class="active" href="#">Newsfeed</a>
  <a href="#">Israel Directory</a>
  <a href="#">International Directory</a>
  <a href="#">Product Directory</a>
  <a href="#">Website Directory</a>
</nav>
<div class="intro">Vorenta.net aggregates new links from 113 websites of the Messianic Community in Israel. <a href="#">Learn more</a></div>

<div class="layout">
  <main class="content">
    <article class="hero ph" role="img" aria-label="Photo of a speaker at a podium">
      <div class="hero-caption">
        <h2>OCTOBER 1, 2013 – A FATEFUL DAY</h2>
        <div class="meta">rootsoffaith.net | September 25, 2013</div>
      </div>
    </article>

    <section class="grid4">
      <div><span class="ph" role="img" aria-label="Film series poster" style="background:linear-gradient(135deg,#c9c2b4,#8c8474)"></span><div class="card-title">The Full Picture Series | Short Films from the ...</div></div>
      <div><span class="ph" role="img" aria-label="Podcast photo" style="background:linear-gradient(135deg,#6c7684,#c0c6ce)"></span><div class="card-title">[Podcast] Washington and Iran: Teaching on the ...</div></div>
      <div><span class="ph" role="img" aria-label="Abstract blue artwork" style="background:linear-gradient(135deg,#1f3c7a,#5e86c9)"></span><div class="card-title">Terms of Mercy - Wellspring Volume 12, Issue 16</div></div>
      <div><span class="ph" role="img" aria-label="News photo from Pakistan" style="background:linear-gradient(135deg,#7a5a42,#c4a888)"></span><div class="card-title">Christians slaughtered in Pakistan; Kenya</div></div>
    </section>

    <section class="grid2">
      <div><span class="ph" role="img" aria-label="Students at a media school" style="background:linear-gradient(135deg,#3e4a5c,#9aa6b6)"></span><div class="card-title">New School Year at Cedar School of Media</div></div>
      <div><span class="ph" role="img" aria-label="Fingertips drawn as smiling friends" style="background:linear-gradient(135deg,#d8b48e,#f2dcc3)"></span><div class="card-title">Living In Israel Blog: Why You Need To Make New Friends</div></div>
    </section>

    <article class="feed-item">
      <span class="ph" role="img" aria-label="City skyline photo" style="background:linear-gradient(135deg,#9fb2c8,#d9d2bf)"></span>
      <div>
        <h3>October 2013: Muslim Arabs and Democracy</h3>
        <div class="source"><i></i>olivebranchnotes.net | Mira Talen | September 23, 2013</div>
        <p>The venerable The Meridian magazine posts a yearly list of most of the nations of the world, judging them in four categories.</p>
      </div>
    </article>
    <article class="feed-item">
      <span class="ph" role="img" aria-label="Portrait photo of the author" style="background:linear-gradient(135deg,#4d5563,#a4abb5)"></span>
      <div>
        <h3>Touch Not God's Anointed or Excuse to not be Accountable?</h3>
        <div class="source"><i></i>Dr. Aaron L. Velde | September 23, 2013</div>
        <p>If a pastor errs, lies, abuses people, or commits sexual immorality is there recourse by the congregation, or does the doctrine "Touch not God's anointed" prevail?</p>
      </div>
    </article>

    <nav class="pager">
      <a href="#">« Prev</a><a class="on" href="#">1</a><a href="#">2</a><a href="#">3</a><a href="#">4</a><a href="#">5</a><a href="#">6</a><a href="#">7</a><a href="#">8</a><a href="#">9</a><a href="#">Next »</a>
    </nav>

    <section>
      <div class="tabs">
        <a class="active" href="#">Newsfeeds</a><a href="#">Israel Directory</a><a href="#">International Directory</a><a href="#">Product Directory</a>
      </div>
      <ul class="latest">
        <li><b>Prayer Watch for Israel Prayer Points - 20 September 2013</b><span>watchmen-il.net | September 20, 2013</span></li>
        <li><b>Sukkot 5774: Build Your Booth and Dwell in It</b><span>olivebranchnotes.net | September 18, 2013</span></li>
        <li><b>Why didn't I Name Names?</b><span>vorentanews.net | September 18, 2013</span></li>
        <li><b>Time to Start Sorting</b><span>jaffagate.net | September 17, 2013</span></li>
        <li><b>[Podcast] Yom Kippur, Televangelists and Syria Update</b><span>rootsoffaith.net | September 17, 2013</span></li>
      </ul>
    </section>
  </main>

  <aside class="sidebar">
    <form class="signup">
      <p>Sign up to Vorenta.net to receive a weekly email that aggregates updates from 113 websites of the Messianic community in Israel.</p>
      <div class="field">Email Address</div>
      <div class="field">Select Country <span>▾</span></div>
      <span class="btn">Sign Up</span>
    </form>

    <div class="ad-banner ph" role="img" aria-label="Advertisement: VoxaLine enterprise quality voicemail at an affordable price"></div>

    <div class="text-ads">
      <div><b>Harborline Inn Express</b><p>Official Site. Stay Smart. Find great comfort &amp; low prices!</p><em>www.harborlineexpress.net</em></div>
      <div><b>Hotel</b><p>Best Hotel Deals At SummitPathTours.net</p><em>summitpathtours.net</em></div>
      <div><b>Harborline Inn Hotels</b><p>Official Site - Book Now. Kids Eat Free. Call 800-555-0142.</p><em>www.harborlineinn.net</em></div>
      <div><b>Aldera Hotel® Deals</b><p>Last Minute Offers &amp; Special Rates Book Our Best Rates!</p><em>www.alderahotels.net</em></div>
      <div class="ad-info">Ad info ▸</div>
    </div>

    <section class="potw">
      <h4>Photo of the Week</h4>
      <span class="ph" role="img" aria-label="Photo of the week"></span>
    </section>

    <div class="text-ads">
      <div><b>Harborline Inn Express</b><p>Official Site. Stay Smart. Find great comfort &amp; low prices!</p><em>www.harborlineexpress.net</em></div>
      <div><b>Hotel</b><p>Best Hotel Deals At SummitPathTours.net</p><em>summitpathtours.net</em></div>
      <div><b>Harborline Inn Hotels</b><p>Official Site - Book Now. Kids Eat Free. Call 800-555-0142.</p><em>www.harborlineinn.net</em></div>
      <div><b>Aldera Hotel® Deals</b><p>Last Minute Offers &amp; Special Rates Book Our Best Rates!</p><em>www.alderahotels.net</em></div>
      <div class="ad-info">Ad info ▸</div>
    </div>
  </aside>
</div>

<footer class="site-footer">
  <nav><a href="#">About</a> | <a href="#">Newsfeed</a> | <a href="#">Israel Directory</a> | <a href="#">International Directory</a> | <a href="#">Product Directory</a> | <a href="#">Website Directory</a> | <a href="#">Contact</a></nav>
  <div>©2006–2013 Vorenta.net All rights reserved</div>
  <div>Vorenta is a Hebrew word that means "community" or "congregation"</div>
</footer>

</body>
</html>
```